Design One page for our website

We need a one page that will works almost like a monthly calendar. On the top of the page the User will be able to click links (menus) that will change the information presented on this new page.

I will send more details for those interested on this project.

Links to two templates that match with our expectations on design level and contain elements that can be used (we bough the the templates for this project, so we can use it) the elements and designs I really like:

http://plumvault.example/item/lumo-premium-admin-template/5182034?WT.ac=solid_search_item&WT.seg_1=solid_search_item&WT.z_author=Brendoxil

http://plumvault.example/item/kelto-metro-style-admin-template/6093815?WT.ac=solid_search_item&WT.seg_1=solid_search_item&WT.z_author=Brendoxil

Let me know if you have any question.

Requirements
Must have
• The design should use elements from two templates, that guarantee the type of design I do expect. Also doing in this way we are trying to avoid to falling outside the normal pattern of the rest of the website.

We need a great design!
Should not have
• We do not want something identical to our draft.

We need someone that make it nicer than we ever could!

We expect the design represent our draft, but we want that it looks much better than it.

```html
<!DOCTYPE html>
<html lang="pt">
<head>
<meta charset="utf-8">
<title>Agenda Mensal</title>
<link rel="stylesheet" href="https://fonts.googleapis.com/css2?family=Source+Sans+3:wght@400;600&display=swap">
<style>
:root{
  --nav-top:#3474c9;
  --nav-bottom:#2a62b6;
  --nav-divider:rgba(255,255,255,.28);
  --ink:#1e1e1e;
  --done:#fbe6e6;
  --done-head:#a9b2e4;
  --today:#bce6f6;
  --today-head:#5bbbe9;
  --plan-head:#43cdb4;
  --label-head:#5aa3e7;
  --group:rgba(0,0,0,.095);
  --line:rgba(0,0,0,.055);
  --future:#fafafa;
  --accent-green:#1f9a3a;
  --cw:calc(795px / 31);
}
*{box-sizing:border-box;margin:0;padding:0}
html,body{width:990px;height:1200px;overflow:hidden;background:#fff}
body{font-family:"Source Sans 3",sans-serif;color:var(--ink)}
.calendar{position:absolute;left:33px;top:73px;width:922px;border:1px solid #d9d9d9}
.tabs{height:23px;display:flex;background:linear-gradient(var(--nav-top),var(--nav-bottom));padding-left:92px}
.tab{display:flex;align-items:center;justify-content:center;color:#fff;font-size:10px;border-left:1px solid var(--nav-divider)}
.tab:last-child{border-right:1px solid var(--nav-divider)}
.toolbar{height:23px;display:grid;grid-template-columns:92px calc(var(--cw)*11) var(--cw) 1fr;font-size:11px;font-weight:600}
.toolbar>div{display:flex;align-items:center;justify-content:center}
.tools{gap:8px;justify-content:flex-start!important;padding-left:12px}
.phase-done{background:var(--done)}
.phase-today{background:var(--today)}
.days,.dates{display:grid;grid-template-columns:92px repeat(31,1fr) 35px}
.days{height:20px;font-size:7px;color:#fff;text-transform:uppercase}
.days span,.dates span{display:flex;align-items:center;justify-content:center}
.days .lbl{background:var(--label-head)}
.days .d{background:var(--done-head)}
.days .t{background:var(--today-head)}
.days .p,.days .tot{background:var(--plan-head)}
.dates{height:27px;font-size:11px;border-bottom:1px solid var(--line)}
.dates .lbl{justify-content:flex-start;padding-left:12px}
.dates .d{background:var(--done)}
.dates .t{background:var(--today)}
.dates .hl{color:var(--accent-green)}
.grid-body{position:relative;background:var(--future)}
.zone{position:absolute;top:0;bottom:0}
.zone-done{left:92px;width:calc(var(--cw)*11);background:var(--done)}
.zone-today{left:calc(92px + var(--cw)*11);width:var(--cw);background:var(--today)}
.col-lines{position:absolute;top:0;bottom:0;left:92px;right:0;
  background:repeating-linear-gradient(to right,transparent 0,transparent calc(var(--cw) - 1px),var(--line) calc(var(--cw) - 1px),var(--line) var(--cw))}
.row{position:relative;height:25px;display:flex;align-items:center;font-size:11px;padding-left:12px;border-bottom:1px solid var(--line)}
.row.group{background:var(--group)}
.row:last-child{border-bottom:0}
</style>
</head>
<body>
<div class="calendar">
  <nav class="tabs">
    <a class="tab" style="width:84px">Instalacoes</a>
    <a class="tab" style="width:76px">Retiradas</a>
    <a class="tab" style="width:71px">Eventos</a>
    <a class="tab" style="width:68px">Mensais</a>
    <a class="tab" style="width:55px">Tudo</a>
    <a class="tab" style="width:68px">$ - Evento</a>
    <a class="tab" style="width:63px">$ -Mensal</a>
    <a class="tab" style="width:55px">$ -Total</a>
  </nav>
  <div class="toolbar">
    <div class="tools">
      <svg width="18" height="16" viewBox="0 0 18 16" aria-label="Imprimir"><rect x="4" y="1" width="10" height="5" fill="#eee" stroke="#777"/><rect x="1" y="6" width="16" height="7" rx="1" fill="#8a8a8a"/><rect x="4" y="10" width="10" height="5" fill="#fff" stroke="#777"/></svg>
      <svg width="18" height="16" viewBox="0 0 18 16" aria-label="Exportar XLS"><rect x="2" y="1" width="11" height="13" fill="#f4f4f4" stroke="#999"/><path d="M7 7h5V4l5 5-5 5v-3H7z" fill="#3aa33a"/></svg>
      <svg width="18" height="16" viewBox="0 0 18 16" aria-label="Exportar PDF"><rect x="2" y="1" width="11" height="13" fill="#f4f4f4" stroke="#999"/><path d="M7 7h5V4l5 5-5 5v-3H7z" fill="#d23a2a"/></svg>
    </div>
    <div class="phase-done">Feito</div>
    <div class="phase-today">Hoje</div>
    <div>Previsto</div>
  </div>
  <div class="days">
    <span class="lbl"></span>
    <span class="d">Sun</span><span class="d">Mon</span><span class="d">Tue</span><span class="d">Wed</span><span class="d">Thu</span><span class="d">Fri</span><span class="d">Sat</span><span class="d">Sun</span><span class="d">Mon</span><span class="d">Tue</span><span class="d">Wed</span>
    <span class="t">Thu</span>
    <span class="p">Fri</span><span class="p">Sat</span><span class="p">Sun</span><span class="p">Mon</span><span class="p">Tue</span><span class="p">Wed</span><span class="p">Thu</span><span class="p">Fri</span><span class="p">Sat</span><span class="p">Sun</span><span class="p">Mon</span><span class="p">Tue</span><span class="p">Wed</span><span class="p">Thu</span><span class="p">Fri</span><span class="p">Sat</span><span class="p">Sun</span><span class="p">Mon</span><span class="p">Tue</span>
    <span class="tot">Totals</span>
  </div>
  <div class="dates">
    <span class="lbl">Date</span>
    <span class="d">1</span><span class="d">2</span><span class="d">3</span><span class="d">4</span><span class="d">5</span><span class="d">6</span><span class="d">7</span><span class="d">8</span><span class="d">9</span><span class="d">10</span><span class="d">11</span>
    <span class="t">12</span>
    <span>13</span><span>14</span><span>15</span><span>16</span><span>17</span><span>18</span><span>19</span><span class="hl">20</span><span>21</span><span>22</span><span>23</span><span>24</span><span>25</span><span>26</span><span>27</span><span>28</span><span>29</span><span>30</span><span>31</span>
    <span></span>
  </div>
  <div class="grid-body">
    <div class="zone zone-done"></div>
    <div class="zone zone-today"></div>
    <div class="col-lines"></div>
    <div class="row group">ITA</div>
    <div class="row">Cabine Sanitaria</div><div class="row">Grade</div><div class="row">Mao de Obra</div><div class="row">Limpa Fossa</div><div class="row">Veiculo</div><div class="row">Container</div>
    <div class="row group">REC</div>
    <div class="row">Cabine Sanitaria</div><div class="row">Grade</div><div class="row">Mao de Obra</div><div class="row">Limpa Fossa</div><div class="row">Veiculo</div><div class="row">Container</div>
    <div class="row group">RIO</div>
    <div class="row">Cabine Sanitaria</div><div class="row">Grade</div><div class="row">Mao de Obra</div><div class="row">Limpa Fossa</div><div class="row">Veiculo</div><div class="row">Container</div>
    <div class="row group">SJC</div>
    <div class="row">Cabine Sanitaria</div><div class="row">Grade</div><div class="row">Mao de Obra</div><div class="row">Limpa Fossa</div><div class="row">Veiculo</div><div class="row">Container</div>
    <div class="row group">VRD</div>
    <div class="row">Cabine Sanitaria</div><div class="row">Grade</div><div class="row">Mao de Obra</div><div class="row">Limpa Fossa</div><div class="row">Veiculo</div><div class="row">Container</div>
    <div class="row group">Hidrojato</div>
    <div class="row">Hidrojato</div>
  </div>
</div>
</body>
</html>
```